Brazilian-Italian food blogger looks for a yummy design for her blog

Ciao everyone! I am looking for a brand new design for my Wordpress food blog, MaReVIA (marevia-example.com). The blog is about my deep love with food and with Bologna. I write particularly for the Brazilian crowd.
I talk about gastronomic curiosities of the town, delicious places and specialties that one can only find here. There are also many posts about my trips around Italy.
I would like the new design to be more sophisticated (or should I say professional?), but friendly at the same time.
If possible, I would like to keep its background very clean (if there are patters related to food, like the way it is now, even better), especially because I post many big colourful photos...
Also, since it is a personal blog, I would love if visitors could see a picture of mine and with a short description right at the homepage.
Thank you so much in advance.
Cheers,
Lidia.

Target Market(s)

Brazilian people interested in Italian culture and gastronomy.

Colors
fcca95

Requirements
Must have
• A neutral background that does not interfere with photos.
• My photo with a short description on the homepage.
Nice to have
• A background that has something to do with food.
Should not have
• It should not look like a girly blog.

```html
<!DOCTYPE html>
<html lang="pt">
<head>
<meta charset="utf-8">
<title>MaReVIA — food blog</title>
<link href="https://fonts.googleapis.com/css2?family=Oswald:wght@400;600&family=Open+Sans:wght@400;600&display=swap" rel="stylesheet">
<style>
:root{
  --orange:#f5a25d;
  --peach:#fcca95;
  --dark:#2b2b2b;
  --darker:#1e1e1e;
  --text:#555;
  --muted:#999;
  --line:#e6e6e6;
  --page:#fbeeee;
  --white:#fff;
}
*{box-sizing:border-box;margin:0;padding:0}
html,body{width:1200px;height:2428px;overflow:hidden}
body{background:linear-gradient(180deg,#fdf3f2,var(--page));font-family:"Open Sans",sans-serif;color:var(--text);position:relative}
.site{position:absolute;left:160px;top:0;width:880px;height:2400px;background:var(--white)}
.nav{position:absolute;left:16px;top:16px;width:848px;height:44px;display:flex;align-items:center;border-bottom:1px solid var(--line)}
.nav a{font-family:"Oswald",sans-serif;font-size:13px;color:var(--dark);text-decoration:none;padding:0 13px;line-height:44px;text-transform:uppercase}
.nav a.current{background:var(--orange);color:var(--white)}
.search{margin-left:auto;display:flex}
.search span{width:150px;height:24px;border:1px solid #ccc}
.search b{width:26px;height:24px;background:var(--dark)}
.banner{position:absolute;left:16px;top:72px;width:848px;height:368px;background:linear-gradient(160deg,#c98a5e,#a05535 55%,#7d3d2a);display:flex;align-items:center;justify-content:center}
.banner .logo{font-family:"Oswald",sans-serif;font-size:64px;color:var(--white);letter-spacing:3px}
.posts{position:absolute;left:16px;top:470px;width:644px}
.post{height:340px;display:flex;gap:12px;border-bottom:1px solid var(--line);padding-top:20px}
.meta{width:60px;display:flex;flex-direction:column;gap:4px}
.date{background:var(--orange);color:var(--white);text-align:center;font-family:"Oswald",sans-serif;padding:6px 0}
.date small{display:block;font-size:11px}
.date strong{display:block;font-size:26px;line-height:1.1}
.comments{background:var(--dark);color:var(--white);text-align:center;font-family:"Oswald",sans-serif;font-size:11px;padding:8px 0;line-height:1.3}
.comments strong{display:block;font-size:20px}
.edit{background:var(--dark);color:var(--white);font-size:10px;text-align:center;padding:4px 0}
.thumb{width:240px;height:240px}
.body{width:320px;padding-left:8px}
.body h2{font-family:"Oswald",sans-serif;font-size:15px;color:var(--dark);text-transform:uppercase;font-weight:600;margin-bottom:10px}
.body .cat{font-size:10px;color:var(--muted);margin-bottom:12px}
.body .cat em{color:var(--orange);font-style:normal}
.body p{font-size:12px;line-height:1.7;margin-bottom:14px}
.more{display:flex;gap:4px}
.more span{background:var(--orange);color:var(--white);font-size:10px;padding:5px 10px;font-family:"Oswald",sans-serif}
.more b{width:24px;background:var(--dark);display:flex;align-items:center;justify-content:center}
.prev{position:absolute;left:16px;top:1892px;display:flex;gap:4px}
.prev b{width:24px;height:24px;background:var(--dark);display:flex;align-items:center;justify-content:center}
.prev span{background:var(--orange);color:var(--white);font-family:"Oswald",sans-serif;font-size:11px;padding:4px 12px}
.sidebar{position:absolute;left:684px;top:470px;width:180px}
.widget-title{background:var(--dark);color:var(--white);font-family:"Oswald",sans-serif;font-size:12px;padding:6px 10px;margin-bottom:12px;text-transform:uppercase}
.about{display:flex;gap:10px;margin-bottom:14px}
.about .portrait{width:70px;height:70px;flex:none;background:linear-gradient(135deg,#b88a6e,#6b4a3a)}
.about p{font-size:10px;line-height:1.5}
.about p strong{color:var(--orange)}
.follow{display:block;background:var(--dark);color:var(--white);font-family:"Oswald",sans-serif;font-size:11px;text-align:center;padding:6px;margin-bottom:18px}
.fanbox{border:1px solid var(--line);padding:8px;margin-bottom:24px}
.fanbox .head{display:flex;gap:6px;align-items:center;font-size:10px;margin-bottom:8px}
.fanbox .head i{width:24px;height:24px;background:var(--orange)}
.faces{display:grid;grid-template-columns:repeat(5,1fr);gap:4px}
.faces i{height:28px;background:#cbb9ae}
.cats li{list-style:none;font-family:"Oswald",sans-serif;font-size:12px;color:var(--dark);padding:6px 0;border-bottom:1px solid var(--line);text-transform:uppercase}
.footer{position:absolute;left:0;top:1964px;width:880px;height:406px;background:var(--dark);display:flex;gap:40px;padding:28px 16px}
.footer h3{font-family:"Oswald",sans-serif;color:var(--white);font-size:16px;margin-bottom:14px;text-transform:uppercase}
.footer li{list-style:none;font-size:10px;color:var(--peach);padding:3px 0;text-transform:uppercase}
.footer .col{width:180px}
.footer .like{width:300px}
.footer .faces{grid-template-columns:repeat(6,1fr)}
.footer .faces i{height:34px;background:#5a5a5a}
.bottom{position:absolute;left:0;top:2370px;width:880px;height:30px;background:var(--darker);display:flex;align-items:center;justify-content:space-between;padding:0 16px;font-size:9px;color:var(--muted)}
.bottom nav a{color:var(--muted);text-decoration:none;margin-left:10px}
</style>
</head>
<body>
<div class="site">
  <nav class="nav">
    <a class="current">Home</a><a>O Blog</a><a>Bella Bo</a><a>Buoni Posti</a><a>Da Lidia</a><a>Fuori Casa</a><a>Contato</a>
    <div class="search"><span></span><b></b></div>
  </nav>
  <header class="banner" role="img" aria-label="Photo of Bologna rooftops in warm terracotta tones">
    <div class="logo">MaReVIA</div>
  </header>

  <main class="posts">
    <article class="post">
      <div class="meta"><div class="date"><small>SEP</small><strong>16</strong><small>2014</small></div><div class="comments"><strong>No</strong>Comment</div><div class="edit">Edit</div></div>
      <div class="thumb" role="img" aria-label="Photo of a plate of fresh pasta" style="background:linear-gradient(135deg,#e9b45a,#c9772f)"></div>
      <div class="body"><h2>Bando de Barato</h2><div class="cat">Posted in <em>Pasta</em></div>
        <p>É impossível contar quantas vezes provei este prato, mas a cada visita ao mercado descubro um novo detalhe. A massa é simples, feita à mão, e o molho chega quente à mesa, perfumado de manteiga e sálvia.</p>
        <div class="more"><span>Read More</span><b><svg width="10" height="10" viewBox="0 0 10 10"><path d="M2 5h6M5 2l3 3-3 3" stroke="#fff" fill="none" stroke-width="1.5"/></svg></b></div></div>
    </article>
    <article class="post">
      <div class="meta"><div class="date"><small>SEP</small><strong>16</strong><small>2014</small></div><div class="comments"><strong>No</strong>Comment</div><div class="edit">Edit</div></div>
      <div class="thumb" role="img" aria-label="Photo of a mortadella sandwich on a counter" style="background:linear-gradient(135deg,#8a6a50,#d9a29a)"></div>
      <div class="body"><h2>Mortadella Bologna</h2><div class="cat">Posted in <em>Mortadela</em></div>
        <p>Um dos grandes símbolos da cidade, a mortadela aparece em todas as vitrines do centro. Fui conhecer uma pequena loja familiar que corta fatias finíssimas na hora e serve com pão quente.</p>
        <div class="more"><span>Read More</span><b><svg width="10" height="10" viewBox="0 0 10 10"><path d="M2 5h6M5 2l3 3-3 3" stroke="#fff" fill="none" stroke-width="1.5"/></svg></b></div></div>
    </article>
    <article class="post">
      <div class="meta"><div class="date"><small>SEP</small><strong>16</strong><small>2014</small></div><div class="comments"><strong>No</strong>Comment</div><div class="edit">Edit</div></div>
      <div class="thumb" role="img" aria-label="Photo of bread and a glass of milk" style="background:linear-gradient(135deg,#d8c4a8,#9c7b58)"></div>
      <div class="body"><h2>Simplesmente Pão e Leite</h2><div class="cat">Posted in <em>Uncategorized</em></div>
        <p>No fim de semana passado visitei uma padaria antiga perto das muralhas. O cheiro de pão saindo do forno tomou a rua inteira, e o leite fresco da manhã completou o café mais gostoso da semana.</p>
        <div class="more"><span>Read More</span><b><svg width="10" height="10" viewBox="0 0 10 10"><path d="M2 5h6M5 2l3 3-3 3" stroke="#fff" fill="none" stroke-width="1.5"/></svg></b></div></div>
    </article>
    <article class="post">
      <div class="meta"><div class="date"><small>SEP</small><strong>16</strong><small>2014</small></div><div class="comments"><strong>No</strong>Comment</div><div class="edit">Edit</div></div>
      <div class="thumb" role="img" aria-label="Photo of a colourful rice salad" style="background:linear-gradient(135deg,#e7d9a0,#7fa05a)"></div>
      <div class="body"><h2>Insalata di Riso della Giulia</h2><div class="cat">Posted in <em>Risi</em></div>
        <p>Quem aqui nunca ficou em dúvida sobre o que levar num piquenique? A salada de arroz da Giulia é fresca, colorida e prática, perfeita para os dias quentes de verão à beira do rio.</p>
        <div class="more"><span>Read More</span><b><svg width="10" height="10" viewBox="0 0 10 10"><path d="M2 5h6M5 2l3 3-3 3" stroke="#fff" fill="none" stroke-width="1.5"/></svg></b></div></div>
    </article>
  </main>

  <div class="prev"><b><svg width="10" height="10" viewBox="0 0 10 10"><path d="M8 5H2M5 2L2 5l3 3" stroke="#fff" fill="none" stroke-width="1.5"/></svg></b><span>Previous Posts</span></div>

  <aside class="sidebar">
    <div class="widget-title">About Me</div>
    <div class="about"><div class="portrait" role="img" aria-label="Portrait photo of the blogger"></div><p><strong>Lidia:</strong> uma brasileira apaixonada por comida, morando em Bologna e contando tudo por aqui.</p></div>
    <span class="follow">Follow the Blog</span>
    <div class="fanbox"><div class="head"><i></i>MaReVIA</div><div class="faces"><i></i><i></i><i></i><i></i><i></i><i></i><i></i><i></i><i></i><i></i></div></div>
    <div class="widget-title">Categories</div>
    <ul class="cats"><li>Mortadela</li><li>Pasta</li><li>Risi</li><li>Sweets</li><li>Uncategorized</li></ul>
  </aside>

  <footer class="footer">
    <div class="col"><h3>Menu</h3><ul><li>Bella Bo</li><li>Buoni Posti</li><li>Curiosidades</li><li>Contato</li><li>Da Lidia</li><li>Fuori Casa</li><li>Lista de restaurantes</li><li>O Blog</li></ul></div>
    <div class="col"><h3>Recent Posts</h3><ul><li>Bando de Barato</li><li>Mortadella Bologna</li><li>Simplesmente Pão e Leite</li><li>Insalata di Riso della Giulia</li><li>Uncategorized</li></ul></div>
    <div class="like"><h3>Like the Blog</h3><div class="faces"><i></i><i></i><i></i><i></i><i></i><i></i><i></i><i></i><i></i><i></i><i></i><i></i></div></div>
  </footer>
  <div class="bottom"><span>© 2014 MaReVIA. Todos os direitos reservados.</span><nav><a>Home</a><a>O Blog</a><a>Bella Bo</a><a>Contato</a></nav></div>
</div>
</body>
</html>
```